Smack you in the face - Landing page for Residential Electrical Repairs (Searchly Ads)

I need an effective landing page for Searchly ads. The ads will target residential electrical repairs. Lighting Outages, Power Outages, Breakers Tripping, Outlets Not Working. I need a strong call to action to Call Us Now! Forms don't work well for us so we only need one form as a last option at the bottom of the page. We only work on homes. the website is https://www.keystone-wiring.com/
email is : support@keystone-wiring.com
Phone 864-555-0172

**This is about one focused service. Electrical Repairs - That includes Partial Power Outages, Outlets Not Working, Tripped Breakers, Electrical Panel repairs, and Fusebox Repairs. The area served will only be Greenville, SC. VIMO is the platform

Target Market(s)

Homeonwers in need of electrical repair

Industry/Entity Type

Residential Electricians

Coding

Coded - Design and coding required

Requirements
Must have
• Strong to action for phone calls, this landing page must grab action fast.
Nice to have
• Social proof with existing 5 start reviews for Searchly, Rateo, TFC, and Friendhub
Should not have
• Should not be form based. I do not like the site's current them, please don't copy it. Make your own.

```html
<!DOCTYPE html>
<html lang="en">
<head>
<meta charset="utf-8">
<title>Keystone Wiring – Residential Electrical Repairs</title>
<link href="https://fonts.googleapis.com/css2?family=Montserrat:wght@400;500;600;700&family=Orbitron:wght@800;900&display=swap" rel="stylesheet">
<style>
:root{
  --teal:#1197c3;
  --teal-dark:#0d7fa6;
  --orange:#e8703a;
  --ink:#1c1c1c;
  --text:#333;
  --muted:#777;
  --gray:#e7e7e7;
  --gold:#f2b01e;
  --white:#fff;
  --line:#dcdcdc;
}
*{box-sizing:border-box;margin:0;padding:0}
html,body{width:1200px;height:3555px;overflow:hidden;background:var(--white)}
body{position:relative;font-family:"Montserrat",sans-serif;color:var(--text)}
.abs{position:absolute}
.btn{position:absolute;display:flex;align-items:center;justify-content:center;border-radius:20px;color:var(--white);font-weight:700;font-size:13px;text-decoration:none}
.btn-teal{background:var(--teal)}
.btn-orange{background:var(--orange)}
.heading{position:absolute;left:0;width:1200px;text-align:center;font-family:"Orbitron",sans-serif;font-weight:900;color:var(--teal);font-size:36px;letter-spacing:2px}
.cta-line{position:absolute;left:0;width:1200px;text-align:center;font-size:19px;color:var(--ink)}
.brand{display:flex;align-items:center;gap:8px;font-family:"Montserrat",sans-serif;font-weight:700;color:var(--ink);font-size:21px;letter-spacing:.5px;white-space:nowrap}
.brand-dot{width:22px;height:22px;border-radius:50%;background:var(--teal);flex:none}
.brand-footer{position:absolute;left:173px;top:3444px;font-size:15px;gap:7px}
.brand-footer .brand-dot{width:18px;height:18px}

/* header */
.site-header{position:absolute;left:0;top:0;width:1200px;height:78px;background:var(--white);z-index:3}
.site-header .brand{position:absolute;left:120px;top:26px}
.header-address{position:absolute;left:678px;top:20px;display:flex;gap:8px;font-size:11px;line-height:17px;color:var(--ink)}
.icon-circle{position:absolute;width:28px;height:28px;border-radius:50%;display:flex;align-items:center;justify-content:center}

/* hero */
.hero-photo{position:absolute;left:0;top:78px;width:1200px;height:370px;background:linear-gradient(110deg,#3b3f44 0%,#5a5d60 35%,#77705a 60%,#a6a54a 80%,#5d6a2f 100%)}
.hero-title{position:absolute;left:0;top:180px;width:1200px;text-align:center;font-family:"Orbitron",sans-serif;font-weight:900;color:var(--white);font-size:35px;line-height:43px;letter-spacing:3px}

/* review platforms */
.platform-card{position:absolute;top:520px;width:197px;height:163px;background:var(--white);border-radius:30px;box-shadow:0 4px 16px rgba(0,0,0,.12);text-align:center}
.platform-name{margin-top:30px;height:34px;display:flex;align-items:center;justify-content:center;font-size:28px;font-weight:700;color:var(--teal)}
.platform-badge{width:96px;height:34px;margin:0 auto;background:#16457a;border-radius:4px}
.platform-meta{margin-top:14px;font-size:11px;color:var(--muted)}
.stars{color:var(--gold);font-size:17px;letter-spacing:3px}
.platform-card .stars{margin-top:14px}

/* services */
.service{position:absolute;width:267px;height:232px}
.service-photo{width:267px;height:200px;border-radius:6px}
.service-label{position:absolute;left:20px;top:185px;width:225px;height:48px;background:var(--white);border-radius:10px;box-shadow:0 3px 10px rgba(0,0,0,.12);display:flex;align-items:center;justify-content:center;font-size:13.5px;font-weight:600;color:var(--ink)}
.service-label.active{background:var(--orange);color:var(--white)}

/* about */
.about-text{position:absolute;left:173px;top:1806px;width:405px;font-size:11px;line-height:16px;color:var(--text)}
.about-text p+p{margin-top:16px}
.about-photo{position:absolute;left:620px;top:1733px;width:407px;height:272px;border-radius:90px 30px 90px 30px;background:linear-gradient(120deg,#8aa14a 0%,#3e4d7c 40%,#24316b 70%,#1c2a5c 100%)}

/* testimonials */
.review{position:absolute;width:267px;height:185px;background:var(--white);border-radius:10px;box-shadow:0 3px 12px rgba(0,0,0,.1);padding:20px 17px}
.review-head{display:flex;align-items:center;gap:10px}
.avatar{width:44px;height:44px;border-radius:50%;border:2px solid var(--teal);display:flex;align-items:center;justify-content:center;color:var(--white);font-weight:600;font-size:18px;flex:none}
.review-who{flex:1}
.review-name{font-size:11px;font-weight:700;color:var(--teal-dark)}
.review-date{font-size:9px;color:var(--muted);margin-top:2px}
.review .stars{font-size:13px;letter-spacing:2px;align-self:flex-start;margin-top:4px}
.review-body{margin-top:12px;font-size:11px;line-height:16px;color:var(--text)}
.review-body u{color:var(--ink)}
.review-source{margin-top:10px;font-size:14px;font-weight:700;color:var(--teal)}
.review-source .platform-badge{width:56px;height:22px;margin:0}

/* form */
.field{position:absolute;border:1px solid var(--line);display:flex;align-items:flex-start;gap:7px;padding:10px 10px;font-size:11px;color:#8a8a8a}
.field svg{flex:none}

/* footer */
.footer-bg{position:absolute;left:0;top:3290px;width:1200px;height:265px;background:linear-gradient(180deg,#ececec 0%,#e2e2e2 100%)}
.footer-item{position:absolute;top:3440px;display:flex;align-items:center;gap:10px;font-size:11.5px;line-height:16px;color:var(--ink)}
.footer-icon{width:30px;height:30px;border-radius:50%;background:var(--teal);display:flex;align-items:center;justify-content:center;flex:none}
.footer-label{color:var(--teal)}
.social{position:absolute;top:3520px;width:18px;height:18px;border-radius:50%;background:var(--ink)}
</style>
</head>
<body>

<header class="site-header">
  <div class="brand"><span class="brand-dot"></span>KEYSTONE WIRING</div>
  <div class="header-address">
    <svg width="22" height="30" viewBox="0 0 22 30"><path d="M11 1C5.5 1 1.5 5 1.5 10.5 1.5 18 11 29 11 29s9.5-11 9.5-18.5C20.5 5 16.5 1 11 1z" fill="var(--teal)"/><circle cx="11" cy="10.5" r="4" fill="#fff"/></svg>
    <div>210 Laurel Ridge Rd, STE 4<br>Greenville, SC 29607</div>
  </div>
  <div class="icon-circle" style="left:878px;top:23px;background:var(--orange)">
    <svg width="14" height="14" viewBox="0 0 24 24"><path d="M6.6 10.8a15 15 0 0 0 6.6 6.6l2.2-2.2a1 1 0 0 1 1-.25 11.4 11.4 0 0 0 3.6.57 1 1 0 0 1 1 1V20a1 1 0 0 1-1 1A17 17 0 0 1 3 4a1 1 0 0 1 1-1h3.5a1 1 0 0 1 1 1c0 1.25.2 2.45.57 3.57a1 1 0 0 1-.25 1z" fill="#fff"/></svg>
  </div>
  <div class="icon-circle" style="left:914px;top:23px;border:1px solid #ccc">
    <svg width="12" height="10" viewBox="0 0 24 18"><rect x="0" y="0" width="24" height="18" rx="2" fill="var(--ink)"/><path d="M1 2l11 8 11-8" stroke="#fff" stroke-width="2" fill="none"/></svg>
  </div>
  <a class="btn btn-teal" style="left:968px;top:22px;width:112px;height:30px" href="tel:8645550172">Call Now</a>
</header>

<section aria-label="Hero">
  <div class="hero-photo" role="img" aria-label="Electrician in a hard hat and safety vest working on a residential breaker panel"></div>
  <svg class="abs" style="left:0;top:78px" width="1200" height="372" viewBox="0 0 1200 372">
    <path d="M0,162 C200,290 450,330 650,320 C850,310 1050,232 1200,160 L1200,188 C1050,272 870,356 650,368 C420,380 180,322 0,262 Z" fill="var(--ink)"/>
    <path d="M0,262 C180,322 420,380 650,368 C870,356 1050,272 1200,188 L1200,372 L0,372 Z" fill="#fff"/>
    <path d="M720,360 C900,336 1080,266 1200,218 L1200,236 C1080,292 900,350 720,364 Z" fill="var(--teal)"/>
  </svg>
  <h1 class="hero-title">RESIDENTIAL<br>ELECTRICAL REPAIRS</h1>
</section>

<section aria-label="Review ratings">
  <div class="platform-card" style="left:173px">
    <div class="platform-name">Searchly</div>
    <div class="platform-meta">4.5 stars &nbsp;|&nbsp; 256 reviews</div>
    <div class="stars">★★★★☆</div>
  </div>
  <div class="platform-card" style="left:393px">
    <div class="platform-name">Friendhub</div>
    <div class="platform-meta">4.5 stars &nbsp;|&nbsp; 256 reviews</div>
    <div class="stars">★★★★☆</div>
  </div>
  <div class="platform-card" style="left:610px">
    <div class="platform-name" style="color:var(--ink)">Rateo</div>
    <div class="platform-meta">4.5 stars &nbsp;|&nbsp; 256 reviews</div>
    <div class="stars">★★★★☆</div>
  </div>
  <div class="platform-card" style="left:829px">
    <div class="platform-name"><div class="platform-badge" role="img" aria-label="TFC accredited business badge"></div></div>
    <div class="platform-meta">4.5 stars &nbsp;|&nbsp; 256 reviews</div>
    <div class="stars">★★★★☆</div>
  </div>
  <p class="cta-line" style="top:711px">Residential Electrical Repairs</p>
  <a class="btn btn-teal" style="left:539px;top:749px;width:112px;height:31px" href="tel:8645550172">Call Now</a>
</section>

<section aria-label="Electrical repairs">
  <svg class="abs" style="left:0;top:860px" width="1200" height="800" viewBox="0 0 1200 800">
    <path d="M200,50 Q600,-22 1000,50 Q600,-6 200,50 Z" fill="var(--teal)"/>
    <path d="M0,95 Q600,10 1200,95 L1200,700 Q600,800 0,700 Z" fill="var(--gray)"/>
    <path d="M200,745 Q600,830 1000,745 Q600,805 200,745 Z" fill="var(--teal)"/>
  </svg>
  <h2 class="heading" style="top:965px">ELECTRICAL REPAIRS</h2>

  <div class="service" style="left:173px;top:1055px">
    <div class="service-photo" role="img" aria-label="Electrician checking a wall fuse box with a flashlight" style="background:linear-gradient(135deg,#e9e6e2 0%,#b39a85 45%,#3a2a22 100%)"></div>
    <div class="service-label">Partial Power Outages</div>
  </div>
  <div class="service" style="left:467px;top:1055px">
    <div class="service-photo" role="img" aria-label="Gloved hands repairing a wall outlet" style="background:linear-gradient(135deg,#f2f2f2 0%,#d9dde4 50%,#5a6a86 100%)"></div>
    <div class="service-label">Outlets Not Working</div>
  </div>
  <div class="service" style="left:760px;top:1055px">
    <div class="service-photo" role="img" aria-label="Hand switching a tripped circuit breaker" style="background:linear-gradient(135deg,#6d3a34 0%,#a8adb4 45%,#d9dde0 100%)"></div>
    <div class="service-label active">Tripped Breakers</div>
  </div>
  <div class="service" style="left:173px;top:1315px">
    <div class="service-photo" role="img" aria-label="Electrician testing an electrical panel with a meter" style="background:linear-gradient(135deg,#3f4a4f 0%,#7c8a8e 50%,#c9b98a 100%)"></div>
    <div class="service-label">Electrical Panel repairs</div>
  </div>
  <div class="service" style="left:467px;top:1315px">
    <div class="service-photo" role="img" aria-label="Electrician working on an outdoor fusebox" style="background:linear-gradient(135deg,#5b3b30 0%,#8c8c8c 45%,#2d3d5c 100%)"></div>
    <div class="service-label">Fusebox Repairs</div>
  </div>
  <p class="cta-line" style="left:760px;width:267px;top:1383px;line-height:22px">Residential Electrical<br>Repairs</p>
  <a class="btn btn-teal" style="left:838px;top:1445px;width:111px;height:31px" href="tel:8645550172">Call Now</a>
</section>

<section aria-label="About us">
  <h2 class="heading" style="top:1730px;left:173px;width:auto;text-align:left">ABOUT US</h2>
  <div class="about-text">
    <p>At Keystone Wiring, EV Chargers, &amp; Generators, your electrical emergency is our urgency. We have Licensed Electricians in Greenville, SC, Raleigh, NC, and Charlotte, NC, ensuring top-tier service for every call.</p>
    <p>We've built our reputation as the go-to Emergency Electrician for homeowners in need. When you find yourself thinking about an "electrician near me," think of us. While many electrical contractors chase after large-scale construction and commercial building projects, we prioritize you – the homeowner.</p>
  </div>
  <a class="btn btn-orange" style="left:173px;top:1968px;width:112px;height:31px" href="tel:8645550172">Call Now</a>
  <div class="about-photo" role="img" aria-label="The Keystone Wiring team in navy shirts standing in front of their service vans"></div>
</section>

<section aria-label="Testimonials">
  <svg class="abs" style="left:0;top:2085px" width="1200" height="800" viewBox="0 0 1200 800">
    <path d="M200,50 Q600,-22 1000,50 Q600,-6 200,50 Z" fill="var(--teal)"/>
    <path d="M0,95 Q600,10 1200,95 L1200,700 Q600,800 0,700 Z" fill="var(--gray)"/>
    <path d="M200,745 Q600,830 1000,745 Q600,805 200,745 Z" fill="var(--teal)"/>
  </svg>
  <h2 class="heading" style="top:2190px">TESTIMONIALS</h2>

  <article class="review" style="left:173px;top:2278px">
    <div class="review-head"><div class="avatar" style="background:#7d8ea3"></div><div class="review-who"><div class="review-name">Derek Lanford</div><div class="review-date">11 days ago</div></div><div class="stars">★★★★★</div></div>
    <p class="review-body">Lorem Ipsum is simply dummy text of the printing and typesetting industry. Lorem Ipsum has been the industry's standard dummy text ever... <u>Read More</u></p>
    <div class="review-source">Searchly</div>
  </article>
  <article class="review" style="left:467px;top:2278px">
    <div class="review-head"><div class="avatar" style="background:#c49a7c"></div><div class="review-who"><div class="review-name">Ruben Castell</div><div class="review-date">12 days ago</div></div><div class="stars">★★★★★</div></div>
    <p class="review-body">Lorem Ipsum is simply dummy text of the printing and typesetting industry. Lorem Ipsum has been the industry's standard dummy text ever... <u>Read More</u></p>
    <div class="review-source">Friendhub</div>
  </article>
  <article class="review" style="left:760px;top:2278px">
    <div class="review-head"><div class="avatar" style="background:#1c3f8f">A</div><div class="review-who"><div class="review-name">A Whitfield</div><div class="review-date">15 days ago</div></div><div class="stars">★★★★★</div></div>
    <p class="review-body">Lorem Ipsum is simply dummy text of the printing and typesetting industry. Lorem Ipsum has been the industry's standard dummy text ever... <u>Read More</u></p>
    <div class="review-source">Searchly</div>
  </article>
  <article class="review" style="left:173px;top:2484px">
    <div class="review-head"><div class="avatar" style="background:#b78a6a"></div><div class="review-who"><div class="review-name">Amara Jobeh</div><div class="review-date">August 13</div></div><div class="stars">★★★★★</div></div>
    <p class="review-body">Lorem Ipsum is simply dummy text of the printing and typesetting industry. Lorem Ipsum has been the industry's standard dummy text ever... <u>Read More</u></p>
    <div class="review-source">Searchly</div>
  </article>
  <article class="review" style="left:467px;top:2484px">
    <div class="review-head"><div class="avatar" style="background:#6aa84f">B</div><div class="review-who"><div class="review-name">brennock</div><div class="review-date">30 days ago</div></div><div class="stars">★★★★★</div></div>
    <p class="review-body">Lorem Ipsum is simply dummy text of the printing and typesetting industry. Lorem Ipsum has been the industry's standard dummy text ever... <u>Read More</u></p>
    <div class="review-source" style="color:var(--ink)">Rateo</div>
  </article>
  <article class="review" style="left:760px;top:2484px">
    <div class="review-head"><div class="avatar" style="background:#c49a7c"></div><div class="review-who"><div class="review-name">Ruben Castell</div><div class="review-date">12 days ago</div></div><div class="stars">★★★★★</div></div>
    <p class="review-body">Lorem Ipsum is simply dummy text of the printing and typesetting industry. Lorem Ipsum has been the industry's standard dummy text ever... <u>Read More</u></p>
    <div class="review-source"><div class="platform-badge" role="img" aria-label="TFC accredited business badge"></div></div>
  </article>

  <p class="cta-line" style="top:2711px">Residential Electrical Repairs</p>
  <a class="btn btn-teal" style="left:460px;top:2751px;width:111px;height:31px" href="tel:8645550172">Call Now</a>
  <a class="btn btn-orange" style="left:578px;top:2751px;width:163px;height:31px" href="#reviews">View all Reviews</a>
</section>

<section aria-label="Quick inquiry">
  <h2 class="heading" style="top:2955px">QUICK INQUIRY</h2>
  <div class="field" style="left:350px;top:3040px;width:243px;height:34px">
    <svg width="12" height="12" viewBox="0 0 24 24"><circle cx="12" cy="8" r="5" fill="none" stroke="var(--teal)" stroke-width="2"/><path d="M3 23c0-5 4-8 9-8s9 3 9 8" fill="none" stroke="var(--teal)" stroke-width="2"/></svg>Name</div>
  <div class="field" style="left:350px;top:3089px;width:243px;height:34px">
    <svg width="12" height="12" viewBox="0 0 24 18"><rect x="1" y="1" width="22" height="16" rx="2" fill="none" stroke="var(--teal)" stroke-width="2"/><path d="M2 2l10 8 10-8" stroke="var(--teal)" stroke-width="2" fill="none"/></svg>Email</div>
  <div class="field" style="left:350px;top:3138px;width:243px;height:34px">
    <svg width="12" height="12" viewBox="0 0 24 24"><rect x="6" y="1" width="12" height="22" rx="2" fill="none" stroke="var(--teal)" stroke-width="2"/></svg>Phone</div>
  <div class="field" style="left:607px;top:3040px;width:244px;height:132px">
    <svg width="12" height="12" viewBox="0 0 24 24"><path d="M3 3h18v13l-5 5H3z" fill="none" stroke="var(--teal)" stroke-width="2"/></svg>Message</div>
  <a class="btn btn-teal" style="left:544px;top:3200px;width:111px;height:31px" href="#submit">Submit</a>
</section>

<footer aria-label="Footer">
  <div class="footer-bg" role="img" aria-label="Faint background photo of an electrician at a panel"></div>
  <svg class="abs" style="left:0;top:3290px" width="1200" height="200" viewBox="0 0 1200 200">
    <path d="M0,0 L1200,0 L1200,10 C800,0 300,60 0,150 Z" fill="#fff"/>
    <path d="M0,110 C300,30 700,5 1200,8 L1200,32 C700,30 320,70 0,160 Z" fill="var(--ink)"/>
    <path d="M0,145 C150,80 300,50 470,40 C300,70 150,120 0,180 Z" fill="var(--teal)"/>
  </svg>
  <div class="brand brand-footer"><span class="brand-dot"></span>KEYSTONE WIRING</div>
  <div class="footer-item" style="left:378px">
    <div class="footer-icon"><svg width="12" height="16" viewBox="0 0 22 30"><path d="M11 1C5.5 1 1.5 5 1.5 10.5 1.5 18 11 29 11 29s9.5-11 9.5-18.5C20.5 5 16.5 1 11 1z" fill="#fff"/></svg></div>
    <div>210 Laurel Ridge Rd, STE 4<br>Greenville, SC 29607</div>
  </div>
  <div class="footer-item" style="left:608px">
    <div class="footer-icon"><svg width="13" height="13" viewBox="0 0 24 24"><path d="M6.6 10.8a15 15 0 0 0 6.6 6.6l2.2-2.2a1 1 0 0 1 1-.25 11.4 11.4 0 0 0 3.6.57 1 1 0 0 1 1 1V20a1 1 0 0 1-1 1A17 17 0 0 1 3 4a1 1 0 0 1 1-1h3.5a1 1 0 0 1 1 1c0 1.25.2 2.45.57 3.57a1 1 0 0 1-.25 1z" fill="#fff"/></svg></div>
    <div><span class="footer-label">Call</span><br>864-555-0172</div>
  </div>
  <div class="footer-item" style="left:773px">
    <div class="footer-icon"><svg width="13" height="10" viewBox="0 0 24 18"><rect x="0" y="0" width="24" height="18" rx="2" fill="#fff"/><path d="M1 2l11 8 11-8" stroke="var(--teal)" stroke-width="2" fill="none"/></svg></div>
    <div><span class="footer-label">Email</span><br>support@keystone-wiring.com</div>
  </div>
  <div class="abs" style="left:173px;top:3510px;width:854px;border-top:1px solid #cfcfcf"></div>
  <p class="abs" style="left:173px;top:3524px;font-size:10px;color:var(--ink)">© 2023 Keystone Wiring. All Right Reserved</p>
  <span class="social" style="left:950px"></span>
  <span class="social" style="left:976px;background:var(--orange);width:20px;height:20px;top:3519px"></span>
  <span class="social" style="left:1004px"></span>
  <svg class="abs" style="left:1044px;top:3515px" width="18" height="22" viewBox="0 0 18 22"><path d="M9 0L18 22 9 16 0 22Z" fill="var(--teal)"/></svg>
</footer>

</body>
</html>
```